Health & Hygeine product flyer

Looking to make a 1 page brochure of products to do with health & sanitisation. Hand Sanitiser, disinfect wipes, Hand Sanitiser dispensers. We are a cleaning company and looking to add these products to our consumables line, and market to existing client base.
I will require our mock up label to be placed on the Hand Sanitiser bottles, and anti bacterial wipes as part of the design

Requirements
Must have
• sharp, crisp, fresh design

```html
<!DOCTYPE html>
<html lang="en">
<head>
<meta charset="utf-8">
<title>Hygiene &amp; Sanitisation Products</title>
<link href="https://fonts.googleapis.com/css2?family=Montserrat:wght@500;600;700;800&family=Oswald:wght@500&family=Nunito:wght@400&display=swap" rel="stylesheet">
<style>
  :root{
    --backdrop:#7a7a7a;
    --navy:#3b3f85;
    --navy-deep:#444683;
    --blue-left:#3f4d8c;
    --blue-right:#5a94c8;
    --panel:#dcdcdc;
    --card:#ffffff;
    --ink:#222222;
    --tick:#4caf50;
    --burst:#e0221b;
  }
  *{margin:0;padding:0;box-sizing:border-box}
  html,body{width:1200px;height:1200px;overflow:hidden;background:var(--backdrop)}
  .flyer{position:absolute;left:146px;top:14px;width:909px;height:1170px;background:var(--panel);overflow:hidden}
  .header{position:absolute;left:0;top:0;width:909px;height:199px;background:linear-gradient(90deg,var(--blue-left) 0%,var(--blue-right) 45%,var(--blue-right) 100%)}
  .brand{position:absolute;left:48px;top:150px;font-family:'Montserrat',sans-serif;font-weight:500;font-size:15px;letter-spacing:3px;color:#fff;white-space:nowrap}
  .brand-dot{position:absolute;left:118px;top:80px;width:44px;height:44px;border:2px solid #fff;border-radius:50%}
  .title{position:absolute;left:270px;top:52px;width:580px;text-align:center;font-family:'Oswald',sans-serif;font-weight:500;font-size:58px;line-height:62px;color:#fff;letter-spacing:-1.5px;white-space:nowrap}
  .card{position:absolute;background:var(--card);border-radius:0 24px 24px 0;width:352px;height:182px}
  .photo{position:absolute;border-radius:8px}
  .info{position:absolute;font-family:'Montserrat',sans-serif;color:var(--navy)}
  .name{font-weight:600;font-size:21px;line-height:24px;white-space:nowrap}
  .name.lg{font-size:23px}
  .sub{font-weight:600;font-size:14px;margin-top:1px}
  .feature{font-family:'Nunito',sans-serif;font-size:14px;color:var(--ink);display:flex;align-items:flex-start;gap:5px;margin-top:5px;line-height:18px}
  .feature svg{flex:none;margin-top:2px}
  .price{position:absolute;height:30px;width:146px;border-radius:15px;background:linear-gradient(90deg,var(--blue-left),var(--blue-right));color:#fff;font-family:'Montserrat',sans-serif;font-weight:800;font-size:18px;line-height:30px;text-align:center}
  .note{position:absolute;font-family:'Montserrat',sans-serif;font-weight:600;font-size:11px;color:var(--ink);width:146px;text-align:center;letter-spacing:.5px}
  .footer{position:absolute;left:0;top:1030px;width:909px;height:140px;background:var(--navy-deep)}
  .burst{position:absolute;left:45px;top:984px;width:156px;height:156px}
  .burst-text{position:absolute;left:45px;top:1020px;width:156px;text-align:center;font-family:'Oswald',sans-serif;font-weight:500;font-size:25px;line-height:28px;color:#fff}
  .delivery{position:absolute;left:40px;top:1112px;width:170px;height:18px;border-radius:9px;background:#fff;font-family:'Oswald',sans-serif;font-size:11.5px;line-height:18px;text-align:center;color:var(--ink)}
  .call{position:absolute;left:216px;top:1054px;font-family:'Montserrat',sans-serif;font-weight:800;font-size:43px;color:#fff;white-space:nowrap}
  .email{position:absolute;left:252px;top:1112px;font-family:'Montserrat',sans-serif;font-weight:600;font-size:20px;color:#fff;white-space:nowrap}
  .certs{position:absolute;left:763px;top:1068px;display:flex;gap:6px}
  .certs span{width:32px;height:60px;border-radius:2px}
</style>
</head>
<body>
<main class="flyer">
  <header class="header">
    <div class="brand-dot"></div>
    <div class="brand">LUMEN CORPORATION</div>
    <h1 class="title">HYGIENE &amp; SANITISATION<br>PRODUCTS</h1>
  </header>

  <section class="card" style="left:74px;top:224px">
    <div class="photo" role="img" aria-label="Pack of disinfectant wipes with company label" style="left:8px;top:34px;width:164px;height:84px;background:linear-gradient(180deg,#eef1f4,#d9dee6)"></div>
    <div class="info" style="left:190px;top:24px;width:160px">
      <div class="name">Disinfectant<br>wipes</div>
      <div class="feature"><svg width="14" height="14" viewBox="0 0 14 14"><circle cx="7" cy="7" r="6" fill="none" stroke="var(--tick)" stroke-width="1.3"/><path d="M4 7.2l2 2 4-4.4" fill="none" stroke="var(--tick)" stroke-width="1.5"/></svg><span>Kills 99.9% of<br>germs</span></div>
    </div>
    <div class="price" style="left:185px;top:125px">$12.95 + GST</div>
  </section>

  <section class="card" style="left:472px;top:224px">
    <div class="photo" role="img" aria-label="500ml pump bottle of hand sanitiser with company label" style="left:28px;top:18px;width:86px;height:150px;background:linear-gradient(180deg,#f2f6fa,#dbe6f0)"></div>
    <div class="info" style="left:139px;top:14px;width:210px">
      <div class="name lg">500ml</div>
      <div class="name">Hand Sanitiser</div>
      <div class="sub">(Pump Bottle)</div>
      <div class="feature"><svg width="14" height="14" viewBox="0 0 14 14"><circle cx="7" cy="7" r="6" fill="none" stroke="var(--tick)" stroke-width="1.3"/><path d="M4 7.2l2 2 4-4.4" fill="none" stroke="var(--tick)" stroke-width="1.5"/></svg><span>75% Alcohol</span></div>
      <div class="feature"><svg width="14" height="14" viewBox="0 0 14 14"><circle cx="7" cy="7" r="6" fill="none" stroke="var(--tick)" stroke-width="1.3"/><path d="M4 7.2l2 2 4-4.4" fill="none" stroke="var(--tick)" stroke-width="1.5"/></svg><span>Kills 99.9% of Germs</span></div>
    </div>
    <div class="price" style="left:145px;top:131px">$13.95 + GST</div>
    <div class="note" style="left:145px;top:166px">(minimum 24 units)</div>
  </section>

  <section class="card" style="left:74px;top:422px">
    <div class="photo" role="img" aria-label="5 litre jug of hand sanitiser with company label" style="left:17px;top:12px;width:111px;height:154px;background:linear-gradient(180deg,#f3f3f3,#dcdcdc)"></div>
    <div class="info" style="left:190px;top:22px;width:160px">
      <div class="name lg">5 Litre</div>
      <div class="name">Hand Sanitiser</div>
      <div class="feature" style="margin-top:10px"><svg width="14" height="14" viewBox="0 0 14 14"><circle cx="7" cy="7" r="6" fill="none" stroke="var(--tick)" stroke-width="1.3"/><path d="M4 7.2l2 2 4-4.4" fill="none" stroke="var(--tick)" stroke-width="1.5"/></svg><span>75% Alcohol</span></div>
      <div class="feature"><svg width="14" height="14" viewBox="0 0 14 14"><circle cx="7" cy="7" r="6" fill="none" stroke="var(--tick)" stroke-width="1.3"/><path d="M4 7.2l2 2 4-4.4" fill="none" stroke="var(--tick)" stroke-width="1.5"/></svg><span>Kills 99.9% of Germs</span></div>
    </div>
    <div class="price" style="left:180px;top:134px">$109 + GST</div>
  </section>

  <section class="card" style="left:472px;top:422px">
    <div class="photo" role="img" aria-label="White wall mounted automatic sanitiser dispenser" style="left:36px;top:20px;width:66px;height:146px;background:linear-gradient(180deg,#f4f4f4,#e0e0e0)"></div>
    <div class="info" style="left:140px;top:22px;width:210px">
      <div class="name" style="font-size:23px;line-height:25px">Wall Mounted<br>Automatic<br>Hand<br>Sanitiser</div>
    </div>
    <div class="price" style="left:143px;top:134px">$149 + GST</div>
  </section>

  <section class="card" style="left:74px;top:622px">
    <div class="photo" role="img" aria-label="Floor standing automatic hand sanitiser unit" style="left:54px;top:18px;width:32px;height:146px;background:linear-gradient(180deg,#efefef,#dedede)"></div>
    <div class="info" style="left:190px;top:11px;width:162px">
      <div class="name" style="font-size:21px;line-height:26px">Floor Stand<br>Hand Sanitiser<br>Unit –<br>Automatic</div>
    </div>
    <div class="price" style="left:181px;top:121px">$389 + GST</div>
  </section>

  <section class="card" style="left:472px;top:622px">
    <div class="photo" role="img" aria-label="Stacks of blue disposable face masks" style="left:32px;top:40px;width:90px;height:112px;background:linear-gradient(180deg,#cfe8f7,#9fcde9)"></div>
    <div class="info" style="left:136px;top:30px;width:210px">
      <div class="name" style="font-size:23px;line-height:25px">Anti-Dust<br>Face Mask</div>
      <div class="feature"><svg width="14" height="14" viewBox="0 0 14 14"><circle cx="7" cy="7" r="6" fill="none" stroke="var(--tick)" stroke-width="1.3"/><path d="M4 7.2l2 2 4-4.4" fill="none" stroke="var(--tick)" stroke-width="1.5"/></svg><span>3 Layer Anti Dust</span></div>
    </div>
    <div class="price" style="left:143px;top:118px">$29.95 + GST</div>
    <div class="note" style="left:143px;top:154px">(50PCS)</div>
  </section>

  <section class="card" style="left:77px;top:824px;width:749px;height:180px">
    <div class="photo" role="img" aria-label="Boxes of nitrile examination gloves in assorted sizes" style="left:77px;top:8px;width:380px;height:160px;background:linear-gradient(135deg,#eeeeee,#9a9a9a 60%,#3a3a4a)"></div>
    <div class="info" style="left:527px;top:34px;width:220px">
      <div class="name" style="font-size:24px;line-height:28px">Nitrite Gloves<br>S/M/L/XL</div>
    </div>
    <div class="price" style="left:527px;top:100px">$22.95 + GST</div>
    <div class="note" style="left:527px;top:140px">(per box)</div>
  </section>

  <footer class="footer"></footer>
  <svg class="burst" viewBox="0 0 100 100" aria-hidden="true">
    <polygon fill="var(--burst)" stroke="#fff" stroke-width="1" points="50,2 55,11 62,3 65,13 74,7 74,17 84,14 81,24 92,24 86,33 96,36 88,43 98,50 88,57 96,64 86,67 92,76 81,76 84,86 74,83 74,93 65,87 62,97 55,89 50,98 45,89 38,97 35,87 26,93 26,83 16,86 19,76 8,76 14,67 4,64 12,57 2,50 12,43 4,36 14,33 8,24 19,24 16,14 26,17 26,7 35,13 38,3 45,11"/>
  </svg>
  <div class="burst-text">PLACE<br>AN ORDER<br>TODAY</div>
  <div class="delivery">Free Delivery for orders over $250</div>
  <div class="call">CALL US 1300 555 019</div>
  <div class="email">OR Email - info@lumencorporation.com.au</div>
  <div class="certs" aria-label="Certification badges">
    <span style="background:#d8262c"></span>
    <span style="background:#1f9a3d"></span>
    <span style="background:#f2c21b"></span>
  </div>
</main>
</body>
</html>
```